Business Card Design for Brambly Consulting

I need business cards for a new company I have started called Brambly Consulting. Brambly Consulting is a new business based out of Columbus Ohio. I will be operating in Ohio as well as nationwide. Brambly Consulting is a professional organization designed to fit your organization's specific needs. We are dedicated to the success of organizations. We handle human resource management, leadership coaching and development, executive training, team building, personality inventories and searches, performance evaluations, temp. services, custom solutions and more. Brambly consulting services a variety of industries such as government agencies, educational systems, board of directors, construction services and more, please visit our website for a full list of services (the website will be important).

I leave the design to you. I am a 45 year old male. I was in the education field for 21 years and 11 years as a superintendent. I like the colors red and black. Don't know what works, I will leave that to you as well. I would like to have it be catchy yet masculine. I have been associated with many organizations over the years both public and private, and will be reaching out to the public and private sector.

I do need a logo...so I leave that to you as well. Company name is Brambly Consulting.

Industry/Entity Type

Construction

Contact Information for Business Card

Gordon T. Brambly, President
Brambly Consulting
47 W.Elmcrest Ave. Suite 318
Arcade at Wexbury Court
Columbus, Ohio 43287

Phone : 330-555-0193
email : gbrambly@bramblyadvisors.example
web : www.bramblyadvisors.example
@bramblyadvisors : @bramblyadvisors
Brambly Consulting : Brambly Consulting

```html
<!DOCTYPE html>
<html lang="en">
<head>
<meta charset="utf-8">
<title>Brambly Consulting – Business Cards</title>
<link rel="stylesheet" href="https://fonts.googleapis.com/css2?family=Orbitron:wght@500;700&family=Michroma&family=Roboto:wght@400;500&display=swap">
<style>
  :root {
    --bg-light: #e4e4e4;
    --bg-dark: #b9b9b9;
    --card: #ffffff;
    --card-edge: #e9e9e9;
    --accent: #1fa6e6;
    --ink: #2e2e2e;
    --ink-soft: #4a4a4a;
  }
  * { margin: 0; padding: 0; box-sizing: border-box; }
  html, body { width: 1200px; height: 947px; overflow: hidden; }
  body {
    background: radial-gradient(ellipse at 40% 35%, var(--bg-light) 0%, var(--bg-dark) 100%);
    font-family: "Roboto", Arial, sans-serif;
    position: relative;
  }
  .card {
    position: absolute;
    left: 280px;
    width: 640px;
    height: 380px;
    background: linear-gradient(135deg, var(--card) 55%, var(--card-edge) 100%);
    border-radius: 28px;
    box-shadow: 0 14px 30px rgba(0,0,0,0.18);
  }
  .card-back { top: 62px; }
  .card-front { top: 500px; }

  .company-name {
    font-family: "Michroma", Arial, sans-serif;
    color: var(--accent);
    font-size: 17px;
    letter-spacing: 2px;
  }
  .card-back .company-name {
    position: absolute;
    top: 50%; left: 0; right: 0;
    transform: translateY(-50%);
    text-align: center;
  }
  .social-links {
    position: absolute;
    right: 40px; bottom: 34px;
    display: flex; gap: 18px;
    list-style: none;
  }
  .social-item {
    display: flex; align-items: center; gap: 6px;
    font-size: 12px; color: var(--ink-soft);
  }
  .social-square {
    width: 16px; height: 16px; background: var(--accent); border-radius: 2px;
  }

  .card-front .company-name {
    position: absolute;
    top: 40px; left: 48px;
  }
  .contact-block {
    position: absolute;
    left: 200px; top: 100px;
    display: flex; flex-direction: column; gap: 20px;
  }
  .contact-row { display: flex; align-items: center; }
  .contact-icon { width: 38px; height: 38px; margin-right: 14px; flex-shrink: 0; }
  .contact-bar {
    width: 4px; align-self: stretch; background: var(--ink); margin-right: 14px;
  }
  .person-name {
    font-family: "Orbitron", Arial, sans-serif;
    font-weight: 700;
    font-size: 26px;
    color: var(--accent);
    letter-spacing: 1px;
    text-transform: uppercase;
    line-height: 1.1;
  }
  .person-title { font-size: 14px; color: var(--ink-soft); margin-top: 4px; }
  .address-line { font-size: 18px; color: var(--ink); line-height: 1.3; letter-spacing: 0.5px; }
  .contact-line { font-size: 15px; color: var(--ink); line-height: 1.35; letter-spacing: 0.5px; }
</style>
</head>
<body>

<section class="card card-back">
  <p class="company-name">Brambly Consulting</p>
  <ul class="social-links">
    <li class="social-item"><span class="social-square"></span>Brambly Consulting</li>
    <li class="social-item"><span class="social-square"></span>@bramblyadvisors</li>
  </ul>
</section>

<section class="card card-front">
  <p class="company-name">Brambly Consulting</p>

  <div class="contact-block">
    <div class="contact-row">
      <svg class="contact-icon" viewBox="0 0 40 40" aria-hidden="true">
        <circle cx="20" cy="12" r="8" fill="var(--accent)"/>
        <path d="M5 38 C5 26 12 22 20 22 C28 22 35 26 35 38 Z" fill="var(--accent)"/>
      </svg>
      <span class="contact-bar"></span>
      <div>
        <p class="person-name">Gordon T. Brambly</p>
        <p class="person-title">President</p>
      </div>
    </div>

    <div class="contact-row">
      <svg class="contact-icon" viewBox="0 0 40 40" aria-hidden="true">
        <path d="M20 2 C11 2 5 9 5 17 C5 27 20 38 20 38 C20 38 35 27 35 17 C35 9 29 2 20 2 Z" fill="var(--accent)"/>
        <circle cx="20" cy="16" r="6" fill="var(--card)"/>
      </svg>
      <span class="contact-bar"></span>
      <div>
        <p class="address-line">47 W.Elmcrest Ave. Suite 318</p>
        <p class="address-line">Arcade at Wexbury Court</p>
        <p class="address-line">Columbus, Ohio 43287</p>
      </div>
    </div>

    <div class="contact-row">
      <svg class="contact-icon" viewBox="0 0 40 40" aria-hidden="true">
        <circle cx="20" cy="20" r="17" fill="var(--accent)"/>
        <g fill="none" stroke="var(--card)" stroke-width="2">
          <ellipse cx="20" cy="20" rx="7" ry="17"/>
          <line x1="20" y1="3" x2="20" y2="37"/>
          <line x1="3" y1="20" x2="37" y2="20"/>
          <path d="M6 11 H34 M6 29 H34"/>
        </g>
      </svg>
      <span class="contact-bar"></span>
      <div>
        <p class="contact-line">330-555-0193</p>
        <p class="contact-line">gbrambly@bramblyadvisors.example</p>
        <p class="contact-line">www.bramblyadvisors.example</p>
      </div>
    </div>
  </div>
</section>

</body>
</html>
```